Pelovina: National Baking Mix Company Needs a Pancake And Waffle Mix Label Design

Hi, we are looking for a front label design for a new pancake and waffle mix. We currently develop and manufacture various dry mixes for crepes, pancakes, waffles, and waffle cones. We are looking to expand our product line into the "all natural" category of foods. This new pancake mix contains the highest quality ingredients including: (whole grain brown rice flour, whole grain oat flour, golden flaxseed meal, whole grain sorghum flour, organic coconut flour, organic coconut sugar, eggs, leavening, vanilla extract, salt, spices.) We are looking for a way to communicate these ingredients to the public by means of claims like one would see on a food label. Here are a few different companies that do it well.
https://toskwelder.com/product/paleo/
https://www.brightquern.com/collections/almond-flour-baking-mixes/products/almond-flour-pancake-waffle-mix
https://morwickoven.com/product/paleo-pancake-waffle-mix/
https://pelovina.com
Our mix is a just add water only mix and consists of whole grains, is gluten free, dairy free, soy free, preservative free, contains no artificial ingredients whatsoever, NON-GMO, kosher, low in sodium, good source of fiber and iron, contains omega-3 fatty acids etc. We need a strong and attractive design that appeals to the customer on a grocery store shelf. This mix is a healthier option compared to traditional pancake/waffle mixes but still provides great taste and texture one would expect from a pancake mix. Label design should be around 4.25"x 6.75" tall ways. We want to utilize what we have to offer in the best way possible.

Target Market(s)

All Natural, Healthy, Pancake Mix. 20yr-50yr olds primariliy

Industry/Entity Type

Grocery Store

Font styles to use
Serif
Sans Serif
Decorative

Colors

Designer to choose colors to be used in the design.

Requirements
Must have
• Name of company "Pelovina", must say "Pancake & Waffle Mix", "Just add water", "gluten free", "dairy free", "whole grains". the rest is up to you!
Nice to have
• I would like to see the claims utilized and promoted in such ways that appeal to the consumer. The all natural category of food is growing and we want to take advantage of that food category.
Should not have
• Should not say "paleo" on label. This mix is within the category but cannot be labeled as such.

```html
<!DOCTYPE html>
<html lang="en">
<head>
<meta charset="utf-8">
<title>Pelovina Pancake &amp; Waffle Mix – Front Label</title>
<link rel="stylesheet" href="https://fonts.googleapis.com/css2?family=Bebas+Neue&display=swap">
<style>
  :root {
    --backdrop: #141416;
    --label-white: #f2f2f2;
    --cocoa: #4a2210;
    --maple-dark: #8b2f14;
    --maple-light: #b65a34;
    --claim-brown: #3f1d0c;
    --photo-deep: #8a5a34;
    --photo-warm: #c99a68;
    --photo-berry: #a8423a;
  }
  html, body {
    margin: 0;
    width: 1200px;
    height: 1200px;
    overflow: hidden;
    background: var(--backdrop);
  }
  .canvas {
    width: 1200px;
    height: 1200px;
    display: block;
  }
  .label-sheet { fill: var(--label-white); }
  .headline {
    font-family: "Bebas Neue", "Arial Narrow", sans-serif;
  }
  .headline-pancake { fill: var(--cocoa); }
  .headline-waffle, .headline-mix { fill: url(#mapleTone); }
  .claim {
    font-family: "Bebas Neue", "Arial Narrow", sans-serif;
    font-size: 38px;
    fill: var(--claim-brown);
  }
  .brand-name {
    font-family: "Bebas Neue", "Arial Narrow", sans-serif;
    font-size: 70px;
    fill: var(--claim-brown);
  }
</style>
</head>
<body>
<svg class="canvas" viewBox="0 0 1200 1200" xmlns="http://www.w3.org/2000/svg">
  <defs>
    <linearGradient id="mapleTone" x1="0" y1="0" x2="1" y2="0">
      <stop offset="0" stop-color="var(--maple-dark)"/>
      <stop offset="1" stop-color="var(--maple-light)"/>
    </linearGradient>
    <linearGradient id="photoTone" x1="0" y1="0" x2="1" y2="1">
      <stop offset="0" stop-color="var(--photo-warm)"/>
      <stop offset="0.45" stop-color="var(--photo-deep)"/>
      <stop offset="0.75" stop-color="var(--photo-berry)"/>
      <stop offset="1" stop-color="var(--photo-deep)"/>
    </linearGradient>
  </defs>

  <rect class="label-sheet" x="280" y="132" width="640" height="940" rx="18"/>

  <g class="headline">
    <text class="headline-pancake" x="332" y="416" font-size="217" textLength="540" lengthAdjust="spacingAndGlyphs">PANCAKE</text>
    <text class="headline-waffle" x="334" y="564" font-size="192" textLength="530" lengthAdjust="spacingAndGlyphs">&amp; WAFFLE</text>
    <text class="headline-mix" x="334" y="668" font-size="132" textLength="166" lengthAdjust="spacingAndGlyphs">MIX</text>
  </g>

  <g class="claims">
    <text class="claim" x="516" y="608" textLength="340" lengthAdjust="spacingAndGlyphs">JUST ADD WATER | GLUTEN FREE</text>
    <text class="claim" x="516" y="648" textLength="304" lengthAdjust="spacingAndGlyphs">DAIRY FREE | WHOLE GRAINS</text>
    <text class="claim" x="516" y="688" textLength="212" lengthAdjust="spacingAndGlyphs">HEALTHY AND TASTY</text>
  </g>

  <text class="brand-name" x="334" y="734" textLength="174" lengthAdjust="spacingAndGlyphs">PELOVINA</text>

  <path class="serving-photo" role="img"
        aria-label="Photo of whole grain waffles topped with strawberries, raspberries, blueberries and syrup"
        d="M332 772 L700 760 Q800 700 868 658 L868 1068 L332 1068 Z"
        fill="url(#photoTone)"/>
</svg>
</body>
</html>
```